Pike Hauling Business Card Design Project

We need a new company business card. We provide professional timber harvesting (logging) and forest management services. I'm open to any creative design. Most company caps and shirts are navy blue and Light grey. Logo does not necessarily have to contain those colors. Logo containing picture of logging equipment, log truck, trees, or logs are acceptable. Be creative. Final logo should communicate our company's pride and professionalism in the East Texas Timber Industry.
Updates

Target Market(s)

Timber owners, sawmills, and forestry professionals

Industry/Entity Type

Business

Requirements
Must have
• Must have Contact Info.
Phone: 936-402-5187
address: PO Box 8412
New Waverly, Tx 77358
www.rbpikehauling.example
rbpikehauling@mailbox.example
Owner: Ross Pike

Or design must leave room for this info.

```html
<!DOCTYPE html>
<html lang="en">
<head>
<meta charset="utf-8">
<title>Pike Hauling – Business Card</title>
<link rel="stylesheet" href="https://fonts.googleapis.com/css2?family=Open+Sans:wght@400;700;800&display=swap">
<style>
  :root {
    --canvas-bg: #e6e4e1;
    --card-front-light: #f4f1ee;
    --card-front-edge: #d9d1cb;
    --card-back: #1c1b1b;
    --ink-brown: #3a2a22;
    --ink-soft: #4a3a32;
    --logo-ink: #ecebe6;
    --sticker-light: #8fd14f;
    --sticker-dark: #4fa82a;
  }
  * { margin: 0; padding: 0; box-sizing: border-box; }
  html, body {
    width: 1200px; height: 918px; overflow: hidden;
    background: var(--canvas-bg);
    font-family: "Open Sans", Arial, sans-serif;
  }
  .canvas { position: relative; width: 1200px; height: 918px; }
  .card {
    position: absolute; top: 299px;
    width: 560px; height: 320px;
    box-shadow: 0 6px 18px rgba(0,0,0,.18);
  }
  .card-front {
    left: 25px;
    background: radial-gradient(ellipse at 58% 45%, #ffffff 0%, var(--card-front-light) 30%, var(--card-front-edge) 100%);
    color: var(--ink-brown);
  }
  .owner-name {
    position: absolute; left: 62px; top: 62px;
    font-size: 36px; font-weight: 800; letter-spacing: .5px;
    line-height: 1;
  }
  .owner-title {
    position: absolute; left: 62px; top: 102px;
    font-size: 15px; font-weight: 400; color: var(--ink-soft);
  }
  .sticker {
    position: absolute; left: 404px; top: 74px;
    width: 130px; height: 130px; border-radius: 50%;
    background: radial-gradient(circle at 40% 35%, var(--sticker-light), var(--sticker-dark));
  }
  .contact-row {
    position: absolute; left: 30px; right: 22px; top: 228px;
    display: flex; justify-content: space-between; align-items: center;
  }
  .contact-item {
    display: flex; align-items: center; gap: 7px;
    font-size: 10.5px; letter-spacing: .8px; color: var(--ink-brown);
  }
  .contact-item svg { width: 14px; height: 14px; flex: none; }
  .card-back {
    left: 615px;
    background: var(--card-back);
    display: flex; align-items: center; justify-content: center;
  }
  .logo-word {
    font-size: 52px; font-weight: 700; letter-spacing: 4px;
    color: var(--logo-ink);
  }
</style>
</head>
<body>
<main class="canvas">
  <section class="card card-front">
    <h1 class="owner-name">Ross Pike</h1>
    <p class="owner-title">Company Owner</p>
    <div class="sticker" role="img" aria-label="Green round greeting sticker with a peeled corner"></div>
    <div class="contact-row">
      <span class="contact-item">
        <svg viewBox="0 0 14 14" aria-hidden="true"><rect x="1" y="3" width="12" height="8" fill="none" stroke="#3a2a22" stroke-width="1.3"/><path d="M1 3 L7 8 L13 3" fill="none" stroke="#3a2a22" stroke-width="1.3"/></svg>
        rbpikehauling@mailbox.example
      </span>
      <span class="contact-item">
        <svg viewBox="0 0 14 14" aria-hidden="true"><path d="M2 5 Q7 1 12 5 L11 7 L9 6 L9 5 Q7 4 5 5 L5 6 L3 7 Z" fill="#3a2a22"/><rect x="3" y="7" width="8" height="5" rx="1" fill="#3a2a22"/></svg>
        936-402-5187
      </span>
      <span class="contact-item">
        <svg viewBox="0 0 14 14" aria-hidden="true"><circle cx="7" cy="7" r="5.6" fill="none" stroke="#3a2a22" stroke-width="1.1"/><ellipse cx="7" cy="7" rx="2.4" ry="5.6" fill="none" stroke="#3a2a22" stroke-width="1"/><path d="M1.4 7 H12.6 M2.5 4.2 H11.5 M2.5 9.8 H11.5" stroke="#3a2a22" stroke-width="1"/></svg>
        www.rbpikehauling.example
      </span>
    </div>
  </section>

  <section class="card card-back">
    <p class="logo-word">LOGO</p>
  </section>
</main>
</body>
</html>
```